Castlewood Funding Partners Loan Officer

I am looking for an upscale business card design with my company logo. I would love to have my picture, QR application code, and NMLS number along with the rest of my contacts information. I am a loan officer for a lending company. I want a card that stands, looks profession, upscale. First looks are everything. It would be nice to incorporate out colors and not just have a white card.

```html
<!DOCTYPE html>
<html lang="en">
<head>
<meta charset="utf-8">
<title>Castlewood Funding Partners – Business Card</title>
<link href="https://fonts.googleapis.com/css2?family=Jost:wght@400;500;600&display=swap" rel="stylesheet">
<style>
  :root {
    --brand-blue: #0a4f9c;
    --brand-green: #0b9a2b;
    --paper: #f6f6f6;
    --ink: #3f3f3f;
    --backdrop: #8d8d8d;
    --white: #ffffff;
  }
  * { margin: 0; padding: 0; box-sizing: border-box; }
  html, body { width: 1200px; height: 1200px; overflow: hidden; }
  body {
    background: var(--backdrop);
    font-family: "Jost", Arial, sans-serif;
    position: relative;
  }
  .card {
    position: absolute;
    left: 262px;
    width: 686px;
    height: 392px;
    overflow: hidden;
  }
  .card-front { top: 165px; background: var(--paper); }
  .card-back { top: 653px; background: var(--brand-blue); }

  .portrait {
    position: absolute;
    left: 0; top: 0;
    width: 324px; height: 392px;
    background: linear-gradient(180deg, #f3f1ee 0%, #d9b393 30%, #c99a78 55%, #1f2f45 75%, #1c2a3e 100%);
  }
  .band {
    position: absolute;
    top: 348px; height: 27px;
  }
  .band-blue { left: 0; width: 295px; background: var(--brand-blue); }
  .band-green {
    left: 297px; right: 0; background: var(--brand-green);
    color: var(--white); font-size: 16px; font-weight: 500;
    letter-spacing: 2.6px; line-height: 27px; padding-left: 64px;
  }

  .wordmark {
    position: absolute;
    display: flex; align-items: center; gap: 10px;
  }
  .wordmark-square { width: 16px; height: 16px; flex: none; }
  .wordmark-name { font-weight: 600; line-height: 1.05; }
  .card-front .wordmark { left: 362px; top: 52px; }
  .card-front .wordmark-square { background: var(--brand-green); }
  .card-front .wordmark-name { color: var(--brand-blue); font-size: 24px; }

  .card-back .wordmark { left: 0; right: 0; top: 160px; justify-content: center; }
  .card-back .wordmark-square { background: var(--brand-green); width: 22px; height: 22px; }
  .card-back .wordmark-name { color: var(--white); font-size: 38px; }

  .contact {
    position: absolute; left: 362px; top: 146px;
    color: var(--ink);
  }
  .person-name {
    color: var(--brand-blue); font-size: 24px; font-weight: 500;
    letter-spacing: -0.2px; line-height: 1.1;
  }
  .person-title { font-size: 16px; margin-top: 1px; }
  .license { font-size: 16px; margin-top: 14px; }
  .address { font-size: 16px; line-height: 1.25; margin-top: 4px; }
  .lines { margin-top: 8px; list-style: none; font-size: 16px; line-height: 1.25; }
  .lines li { display: flex; align-items: center; gap: 9px; }
  .lines svg { width: 15px; height: 15px; fill: var(--brand-blue); flex: none; }
</style>
</head>
<body>
  <section class="card card-front">
    <div class="portrait" role="img" aria-label="Portrait photo of the loan officer"></div>

    <div class="wordmark">
      <span class="wordmark-square"></span>
      <span class="wordmark-name">Castlewood<br>Funding Partners</span>
    </div>

    <div class="contact">
      <h1 class="person-name">DANIEL BROOKS</h1>
      <p class="person-title">Founder &amp; CEO</p>
      <p class="license">NMLS #48213</p>
      <p class="address">4120 Birchfield Road<br>Juneau, Alaska 99801</p>
      <ul class="lines">
        <li>
          <svg viewBox="0 0 24 24" aria-hidden="true"><path d="M6.6 10.8a15.1 15.1 0 0 0 6.6 6.6l2.2-2.2c.3-.3.7-.4 1-.2 1.1.4 2.3.6 3.6.6.6 0 1 .4 1 1V20c0 .6-.4 1-1 1A17 17 0 0 1 3 4c0-.6.4-1 1-1h3.5c.6 0 1 .4 1 1 0 1.3.2 2.5.6 3.6.1.3 0 .7-.2 1z"/></svg>
          555-201-4870
        </li>
        <li>
          <svg viewBox="0 0 24 24" aria-hidden="true"><path d="M7 1h10a2 2 0 0 1 2 2v18a2 2 0 0 1-2 2H7a2 2 0 0 1-2-2V3a2 2 0 0 1 2-2zm0 3v14h10V4zm5 15.5a1 1 0 1 0 0 2 1 1 0 0 0 0-2z"/></svg>
          555-309-6124
        </li>
        <li>
          <svg viewBox="0 0 24 24" aria-hidden="true"><path d="M2 5h20v14H2zm2 2v.5l8 5 8-5V7zm0 2.8V17h16V9.8l-8 5z"/></svg>
          info@castlewoodfp.com
        </li>
      </ul>
    </div>

    <div class="band band-blue"></div>
    <div class="band band-green">www.castlewoodfp.com</div>
  </section>

  <section class="card card-back">
    <div class="wordmark">
      <span class="wordmark-square"></span>
      <span class="wordmark-name">Castlewood Funding Partners</span>
    </div>
  </section>
</body>
</html>
```